We need a business card design for a new brand within our existing financial marketing business. Our new brand is www.qalvenport.co.uk

We attach various logo files - please use the version that will produce the sharpest image on the business card.

We are flexible about shape of card etc. Please think outside the box as to what goes on front and what goes on back of the card.

The card needs to be corporate, but really catch the eye ( e.g. premium translucent cards on plastic etc or metal cards or shiny surface etc )

We want to be able to amend the card (once the design has been agreed ) to add additional staff details, but the text to go on it will be generic

Details to go on card ( for the first generic one) are fairly minimal as we don't like cluttered business cards:-

Owen Tagget
Managing Director

Mobile: 07852 418 207
Email: o.tagget@qalvenport.co.uk

Financial

```html
<!DOCTYPE html>
<html lang="en">
<head>
<meta charset="utf-8">
<title>qalvenport business card</title>
<link href="https://fonts.googleapis.com/css2?family=Lato:wght@300;400;700&display=swap" rel="stylesheet">
<style>
  :root {
    --backdrop: #e7e7e7;
    --card-white: #fbfbfb;
    --brand-blue: #0b5ea8;
    --blue-light: #0a78b4;
    --blue-deep: #004891;
    --ink: #1d1d1d;
    --divider: #3a3a3a;
  }
  * { margin: 0; padding: 0; box-sizing: border-box; }
  html, body {
    width: 1200px; height: 720px; overflow: hidden;
    background: var(--backdrop);
    font-family: "Lato", Arial, sans-serif;
  }
  .canvas { position: relative; width: 1200px; height: 720px; }
  .card {
    position: absolute; top: 241px;
    width: 420px; height: 240px;
  }
  .card--front { left: 147px; background: var(--card-white); }
  .card--back {
    left: 633px;
    background: linear-gradient(135deg, var(--blue-light) 0%, var(--blue-deep) 100%);
    display: flex; align-items: center; justify-content: center;
  }
  .wordmark {
    font-family: "Lato", Arial, sans-serif;
    font-weight: 300;
    letter-spacing: 0.5px;
    white-space: nowrap;
  }
  .card--front .wordmark {
    position: absolute; left: 24px; top: 102px;
    font-size: 31px; line-height: 36px;
    color: var(--brand-blue);
  }
  .card--back .wordmark {
    font-size: 48px; line-height: 1;
    color: #ffffff;
    transform: translateY(-2px);
  }
  .divider {
    position: absolute; left: 210px; top: 79px;
    width: 1.5px; height: 80px;
    background: linear-gradient(to bottom, transparent, var(--divider) 20%, var(--divider) 80%, transparent);
  }
  .contact { position: absolute; left: 226px; top: 83px; color: var(--ink); }
  .contact__name {
    font-weight: 700; font-size: 13.5px; line-height: 16px;
    color: var(--brand-blue);
  }
  .contact__role { font-size: 10px; line-height: 12px; margin-bottom: 8px; }
  .contact__list { list-style: none; }
  .contact__item {
    display: flex; align-items: center;
    font-size: 10px; line-height: 12px; height: 12px;
  }
  .contact__icon { width: 10px; height: 10px; margin-right: 10px; flex: none; }
</style>
</head>
<body>
<main class="canvas">
  <section class="card card--front">
    <div class="wordmark">qalvenport</div>
    <div class="divider"></div>
    <div class="contact">
      <p class="contact__name">Owen Tagget</p>
      <p class="contact__role">Managing Director</p>
      <ul class="contact__list">
        <li class="contact__item">
          <svg class="contact__icon" viewBox="0 0 10 10" aria-hidden="true">
            <rect x="2.5" y="0.5" width="5" height="9" rx="1" fill="none" stroke="#0b5ea8" stroke-width="1"/>
            <line x1="4.3" y1="8" x2="5.7" y2="8" stroke="#0b5ea8" stroke-width="0.8"/>
          </svg>
          07852 418 207
        </li>
        <li class="contact__item">
          <svg class="contact__icon" viewBox="0 0 10 10" aria-hidden="true">
            <rect x="0.5" y="2" width="9" height="6.5" fill="#0b5ea8"/>
            <polyline points="0.5,2 5,5.8 9.5,2" fill="none" stroke="#fff" stroke-width="0.8"/>
          </svg>
          o.tagget@qalvenport.co.uk
        </li>
        <li class="contact__item">
          <svg class="contact__icon" viewBox="0 0 10 10" aria-hidden="true">
            <rect x="0.5" y="1.5" width="9" height="5.5" fill="none" stroke="#0b5ea8" stroke-width="1"/>
            <line x1="5" y1="7" x2="5" y2="8.8" stroke="#0b5ea8" stroke-width="1"/>
            <line x1="3" y1="9" x2="7" y2="9" stroke="#0b5ea8" stroke-width="1"/>
          </svg>
          www.qalvenport.co.uk
        </li>
      </ul>
    </div>
  </section>
  <section class="card card--back">
    <div class="wordmark">qalvenport</div>
  </section>
</main>
</body>
</html>
```